TalkBridge - Language Coaching Services

Sleek, innovative, trendy design for Language Coaching business.

TalkBridge is a new UK based company that provides Language Coaching services. We offer highly personalized on-line and face to face language courses. We also impart learning techniques workshops based on the latest neuroscience research for second-language acquisition.

Target Market(s)

Industry/Entity Type

Consulting

Contact Information for Business Card

TalkBridge
ElenaVT@talkbridge-demo.co.uk
TalkBridge-demo.co.uk
London, UK

Font styles to use
Sans Serif

```html
<!DOCTYPE html>
<html lang="en">
<head>
<meta charset="utf-8">
<title>TalkBridge Business Card</title>
<link rel="stylesheet" href="https://fonts.googleapis.com/css2?family=Oswald:wght@500&family=PT+Sans:wght@400&display=swap">
<style>
  :root {
    --stage: #2b2b2d;
    --card-back: #242426;
    --card-front: #19191b;
    --brand-blue: #1f8fc4;
    --name-blue: #5b8fe0;
    --rule-blue: #4f86d8;
    --text-light: #eceef2;
  }
  * { margin: 0; padding: 0; box-sizing: border-box; }
  html, body {
    width: 1200px; height: 1200px; overflow: hidden;
    background: var(--stage);
    font-family: "PT Sans", sans-serif;
  }
  .canvas {
    width: 1200px; height: 1200px;
    display: flex; flex-direction: column;
    align-items: center; justify-content: center; gap: 60px;
  }
  .card {
    position: relative;
    width: 875px; height: 500px;
    box-shadow: 0 18px 40px rgba(0,0,0,.45);
  }
  .card--back { background: var(--card-back); display: flex; align-items: center; justify-content: center; }
  .card--front { background: var(--card-front); }

  .brand { display: flex; align-items: center; gap: 18px; color: var(--brand-blue); }
  .brand__dot {
    width: 46px; height: 46px; border-radius: 50%;
    border: 6px solid var(--brand-blue);
  }
  .brand__name { font-size: 46px; font-weight: 400; letter-spacing: 1px; }

  .brand--stacked {
    position: absolute; left: 70px; top: 140px; width: 400px;
    flex-direction: column; gap: 26px;
  }
  .brand--stacked .brand__dot { width: 150px; height: 150px; border-width: 9px; }
  .brand--stacked .brand__name { font-size: 60px; letter-spacing: 2px; }

  .divider {
    position: absolute; left: 530px; top: 90px;
    width: 3px; height: 320px; background: var(--rule-blue);
  }
  .contact { position: absolute; left: 575px; top: 120px; color: var(--text-light); }
  .contact__name {
    font-family: "Oswald", sans-serif; font-weight: 500;
    font-size: 38px; color: var(--name-blue); line-height: 1.05;
  }
  .contact__title { font-size: 21px; margin-bottom: 18px; }
  .contact__address { font-size: 21px; line-height: 1.3; margin-bottom: 14px; }
  .contact__list { list-style: none; font-size: 21px; line-height: 1.45; }
  .contact__list li { display: flex; align-items: center; gap: 14px; }
  .contact__list svg { width: 16px; height: 16px; flex: none; fill: var(--rule-blue); }
</style>
</head>
<body>
<main class="canvas">
  <section class="card card--back">
    <div class="brand">
      <span class="brand__dot"></span>
      <span class="brand__name">TalkBridge</span>
    </div>
  </section>

  <section class="card card--front">
    <div class="brand brand--stacked">
      <span class="brand__dot"></span>
      <span class="brand__name">TalkBridge</span>
    </div>
    <div class="divider"></div>
    <div class="contact">
      <h1 class="contact__name">ELENA TORRES</h1>
      <p class="contact__title">President &amp; CEO</p>
      <p class="contact__address">Harbourfield Partners, LLC<br>48 Kestrel Lane, Ste 12 London</p>
      <ul class="contact__list">
        <li><svg viewBox="0 0 16 16"><path d="M3 1l3 3-1.5 2a9 9 0 0 0 5.5 5.5L12 10l3 3-2 2C7 15 1 9 1 3z"/></svg>+(000) -000- 0000</li>
        <li><svg viewBox="0 0 16 16"><path d="M1 3h14v10H1z M2 4l6 5 6-5" /></svg>Info@talkbridge-demo.co.uk</li>
        <li><svg viewBox="0 0 16 16"><circle cx="8" cy="8" r="7"/></svg>www.talkbridge-demo.co.uk</li>
      </ul>
    </div>
  </section>
</main>
</body>
</html>
```